School Hallway Magnetic Display Design for school values

I am looking for a someone to help me design a magnetic hallway display that will hang in the hallway of our small school. There are several elements, including 1. 6ft by 4ft designed magnetic bulletin board, 2. Magnets that will stick to the board. See attachment for which elements belong where. The display will be for our TAVRON program, which rewards students for demonstrating our school values. We want the display to be beautiful and interactive. We are also rebranding, so we want the design to align with our new fonts and colors. In the attached PDF is an outline of our new brand guidelines. Unfortunately, we don't have the color codes, but I'm hoping that you can match the colors listed. Attached are elements to be used on the board, but please use your creativity to make it more dynamic and visually appealing. For example, the star magnets could be another shape. The TAVRON magnets must remain the same. I've included two photos of boards at other schools that inspired this project.

Target Market(s)

School Community

Industry/Entity Type

Education

Requirements
Should not have
• School Logo

```html
<!DOCTYPE html>
<html lang="en">
<head>
<meta charset="utf-8">
<title>TAVRON of the Month – Hallway Values Board</title>
<link rel="stylesheet" href="https://fonts.googleapis.com/css2?family=Source+Serif+4:wght@600&family=Open+Sans:wght@700&display=swap">
<style>
  :root {
    --leaf: #5e9a4e;
    --leaf-light: #72a960;
    --fern: #6a9a58;
    --lime: #dcd74a;
    --lime-light: #e6df58;
    --sky: #84aec0;
    --sky-light: #92b7c6;
    --sun: #f0c84a;
    --sun-light: #f4d25a;
    --aqua: #8cc2cc;
    --aqua-light: #9fd0d6;
    --panel: #f6f8f5;
    --ink: #222822;
    --thermo-fill: #8cc860;
    --hex-gold: #f2bf36;
    --hex-green: #4f8a4a;
    --hex-blue: #6aa2cc;
    --star: #f3c433;
    --white: #ffffff;
  }
  * { margin: 0; padding: 0; box-sizing: border-box; }
  html, body { width: 1200px; height: 800px; overflow: hidden; background: #f2f2f0; }
  .board {
    position: relative;
    width: 1200px; height: 800px;
    background: linear-gradient(120deg, #9cc46a 0%, #5e9a4e 25%, #cfd24a 50%, #6fae5a 72%, #e0d24c 100%);
  }
  .board-panel {
    position: absolute;
    left: 32px; top: 36px; right: 32px; bottom: 30px;
    background: var(--panel);
  }
  .title-banner {
    position: absolute;
    left: 103px; top: 30px;
    width: 992px; height: 112px;
    border-radius: 56px;
    background: linear-gradient(90deg, var(--leaf), var(--leaf-light) 50%, var(--leaf));
    display: flex; align-items: center; justify-content: center;
  }
  .title-banner h1 {
    font-family: "Source Serif 4", Georgia, serif;
    font-weight: 600;
    font-size: 76px;
    color: var(--white);
    letter-spacing: -0.5px;
  }
  .value-list {
    position: absolute;
    left: 144px; top: 197px;
    list-style: none;
  }
  .value-tag {
    width: 275px; height: 67px;
    margin-bottom: 12px;
    border-radius: 4px;
    display: flex; align-items: center; justify-content: center;
    font-family: "Open Sans", Arial, sans-serif;
    font-weight: 700;
    font-size: 35px;
    color: var(--white);
    box-shadow: 0 2px 3px rgba(0,0,0,0.18);
  }
  .value-tag.simplicity { background: linear-gradient(var(--leaf-light), var(--leaf)); }
  .value-tag.peace { background: linear-gradient(var(--lime-light), var(--lime)); }
  .value-tag.integrity { background: linear-gradient(var(--sky-light), var(--sky)); }
  .value-tag.community { background: linear-gradient(#78a866, var(--fern)); }
  .value-tag.equality { background: linear-gradient(var(--sun-light), var(--sun)); }
  .value-tag.stewardship { background: linear-gradient(var(--aqua-light), var(--aqua)); }
  .goal-thermometer { position: absolute; left: 930px; top: 182px; }
  .star-magnets { position: absolute; left: 450px; top: 642px; }
  .badge-magnets { position: absolute; left: 706px; top: 648px; }
</style>
</head>
<body>
<main class="board">
  <div class="board-panel"></div>

  <header class="title-banner">
    <h1>TAVRON of the Month</h1>
  </header>

  <ul class="value-list">
    <li class="value-tag simplicity">Simplicity</li>
    <li class="value-tag peace">Peace</li>
    <li class="value-tag integrity">Integrity</li>
    <li class="value-tag community">Community</li>
    <li class="value-tag equality">Equality</li>
    <li class="value-tag stewardship">Stewardship</li>
  </ul>

  <svg class="goal-thermometer" width="126" height="440" viewBox="0 0 126 440" aria-label="Progress thermometer">
    <path d="M38 18 a24 18 0 0 1 48 0 V318 a56 56 0 1 1 -48 0 Z" fill="var(--white)"/>
    <path d="M41 148 H83 V320 a53 53 0 1 1 -42 0 Z" fill="var(--thermo-fill)"/>
    <path d="M38 18 a24 18 0 0 1 48 0 V318 a56 56 0 1 1 -48 0 Z" fill="none" stroke="var(--ink)" stroke-width="6"/>
    <g stroke="var(--ink)" stroke-width="4">
      <line x1="64" y1="27" x2="86" y2="27"/>
      <line x1="72" y1="52" x2="86" y2="52"/>
      <line x1="64" y1="78" x2="86" y2="78"/>
      <line x1="72" y1="104" x2="86" y2="104"/>
      <line x1="64" y1="130" x2="86" y2="130"/>
      <line x1="72" y1="156" x2="86" y2="156"/>
      <line x1="64" y1="182" x2="86" y2="182"/>
      <line x1="72" y1="208" x2="86" y2="208"/>
      <line x1="64" y1="234" x2="86" y2="234"/>
      <line x1="72" y1="260" x2="86" y2="260"/>
      <line x1="64" y1="286" x2="86" y2="286"/>
    </g>
    <path d="M84 356 a22 22 0 0 1 -4 36" fill="none" stroke="var(--ink)" stroke-width="5" stroke-linecap="round"/>
  </svg>

  <svg class="star-magnets" width="280" height="132" viewBox="0 0 280 132" aria-label="Star magnets">
    <defs>
      <path id="star" d="M0 -36 L10.6 -14.6 L34.2 -11.1 L17.1 5.5 L21.2 29.1 L0 18 L-21.2 29.1 L-17.1 5.5 L-34.2 -11.1 L-10.6 -14.6 Z" fill="var(--star)"/>
    </defs>
    <use href="#star" x="36" y="38"/>
    <use href="#star" x="118" y="38"/>
    <use href="#star" x="200" y="38"/>
    <use href="#star" x="78" y="98"/>
    <use href="#star" x="160" y="98"/>
    <use href="#star" x="240" y="98"/>
  </svg>

  <svg class="badge-magnets" width="360" height="88" viewBox="0 0 360 88" aria-label="Value badge magnets">
    <defs>
      <path id="hex" d="M0 -42 L36 -21 V21 L0 42 L-36 21 V-21 Z"/>
    </defs>
    <g transform="translate(39 44)">
      <use href="#hex" fill="var(--hex-gold)"/>
      <path d="M0 -22 L6.5 -9 L21 -7 L10.5 3.5 L13 18 L0 11 L-13 18 L-10.5 3.5 L-21 -7 L-6.5 -9 Z" fill="var(--white)"/>
    </g>
    <g transform="translate(133 44)">
      <use href="#hex" fill="var(--hex-green)"/>
      <path d="M0 16 C-30 -4 -18 -24 0 -10 C18 -24 30 -4 0 16 Z" fill="var(--white)"/>
    </g>
    <g transform="translate(227 44)">
      <use href="#hex" fill="var(--hex-gold)"/>
      <g fill="var(--white)">
        <path d="M0 -18 C9 -8 9 6 0 12 C-9 6 -9 -8 0 -18 Z"/>
        <path d="M-4 12 C-16 10 -20 0 -18 -8 C-10 -4 -6 4 -4 12 Z"/>
        <path d="M4 12 C16 10 20 0 18 -8 C10 -4 6 4 4 12 Z"/>
        <rect x="-12" y="14" width="24" height="3" rx="1.5"/>
      </g>
    </g>
    <g transform="translate(321 44)">
      <use href="#hex" fill="var(--hex-blue)"/>
      <g fill="none" stroke="var(--white)" stroke-width="4" stroke-linecap="round" stroke-linejoin="round">
        <path d="M-24 -4 L-12 -12 L2 -6"/>
        <path d="M24 -4 L12 -12 L-2 -2 L4 4"/>
        <path d="M-18 2 L-4 14 L8 6 L18 0"/>
      </g>
    </g>
  </svg>
</main>
</body>
</html>
```